Corporate Business Card

Very professional, Modern, Not to busy, include phone address email, website
(253) 555-0174, 61807 19th Street N, Halvern, OR 98517, marcus@kestrelbayholding.com, brelvanindustries.com

Target Market(s)

Manufacturing

Industry/Entity Type

Aero, machining, manufacturing, Off road racing

Contact Information for Business Card

Phone, address email, website

```html
<!DOCTYPE html>
<html lang="en">
<head>
<meta charset="utf-8">
<title>Brelvan Industries — Business Card</title>
<link rel="stylesheet" href="https://fonts.googleapis.com/css2?family=Poppins:wght@400;500;600;800&display=swap">
<style>
  :root {
    --bg: #3a3b3e;
    --navy: #183468;
    --navy-line: #22407d;
    --red: #d6222d;
    --red-deep: #9a2540;
    --white: #ffffff;
    --ink: #1c1c1f;
    --faint-blue: #eef0f6;
    --faint-red: #fbeeee;
  }
  * { margin: 0; padding: 0; box-sizing: border-box; }
  html, body { width: 1200px; height: 900px; overflow: hidden; }
  body {
    background: var(--bg);
    font-family: "Poppins", sans-serif;
    position: relative;
  }
  .card {
    position: absolute;
    width: 560px;
    height: 320px;
    border-radius: 22px;
    overflow: hidden;
  }
  .card--front { left: 110px; top: 100px; background: var(--navy); }
  .card--back { left: 530px; top: 480px; background: var(--white); }
  .card__art { position: absolute; inset: 0; width: 100%; height: 100%; }

  .wordmark { position: absolute; line-height: 1; }
  .wordmark__name {
    font-weight: 800;
    font-size: 46px;
    letter-spacing: 1px;
    display: block;
  }
  .wordmark__sub {
    font-weight: 500;
    font-size: 14px;
    letter-spacing: 1px;
    display: block;
    text-align: right;
    margin-top: 2px;
  }
  .card--front .wordmark { left: 140px; top: 108px; color: var(--white); }
  .card--back .wordmark { left: 52px; top: 64px; color: var(--navy); }

  .website {
    position: absolute;
    left: 215px;
    top: 252px;
    color: var(--white);
    font-weight: 600;
    font-size: 18px;
    letter-spacing: 0.3px;
  }
  .contact {
    position: absolute;
    left: 306px;
    top: 160px;
    color: var(--ink);
    font-size: 14px;
    line-height: 1.75;
    font-style: normal;
  }
</style>
</head>
<body>

  <section class="card card--front" aria-label="Card front">
    <svg class="card__art" viewBox="0 0 560 320" aria-hidden="true">
      <polygon points="384,108 560,108 560,118 376,118" fill="var(--red-deep)"/>
      <polygon points="384,128 560,128 560,138 376,138" fill="var(--red-deep)"/>
      <line x1="140" y1="190" x2="290" y2="190" stroke="var(--white)" stroke-width="2"/>
      <rect x="440" y="212" width="120" height="3" fill="var(--red)"/>
      <rect x="0" y="298" width="180" height="4" fill="var(--white)"/>
    </svg>
    <div class="wordmark">
      <span class="wordmark__name">BRELVAN</span>
      <span class="wordmark__sub">Industries</span>
    </div>
    <p class="website">www.brelvanindustries.com</p>
  </section>

  <section class="card card--back" aria-label="Card back">
    <svg class="card__art" viewBox="0 0 560 320" aria-hidden="true">
      <polygon points="400,0 425,0 185,320 160,320" fill="var(--faint-blue)"/>
      <polygon points="440,0 470,0 230,320 200,320" fill="var(--faint-red)"/>
      <polygon points="480,0 505,0 265,320 240,320" fill="var(--faint-red)"/>
      <line x1="62" y1="156" x2="210" y2="156" stroke="var(--navy)" stroke-width="2"/>
      <polygon points="0,176 258,176 270,194 0,194" fill="var(--navy-line)"/>
      <polygon points="0,206 274,206 286,224 0,224" fill="var(--red)"/>
      <polygon points="0,236 290,236 302,254 0,254" fill="var(--red)"/>
    </svg>
    <div class="wordmark">
      <span class="wordmark__name">BRELVAN</span>
      <span class="wordmark__sub">Industries</span>
    </div>
    <address class="contact">
      (541) 555-0174, 61807 19th<br>
      Street N, Halvern, OR 98517<br>
      marcus@kestrelbayholding.com
    </address>
  </section>

</body>
</html>
```